Medical Company in need of a Modern Flyer design for new Wound Care clinic.

Tri-Fold modern flyer design for our Woundcare company. Logo and description of services can be found on our website; https://www.birchline-woundcare.com/

```html
<!DOCTYPE html>
<html lang="en">
<head>
<meta charset="utf-8">
<title>Birchline Woundcare Tri-Fold</title>
<link rel="stylesheet" href="https://fonts.googleapis.com/css2?family=Poppins:wght@300;400;500;600;700&display=swap">
<style>
  :root{
    --gold:#d9a43c;
    --gold-dark:#b8862b;
    --gold-light:#f2c46a;
    --ink:#222222;
    --ink-soft:#3a3a3a;
    --panel-gray:#f3f3f3;
    --page-bg:#e6e6e6;
    --paper:#ffffff;
  }
  *{margin:0;padding:0;box-sizing:border-box;}
  html,body{width:1200px;height:3146px;overflow:hidden;}
  body{background:var(--page-bg);font-family:"Poppins",sans-serif;color:var(--ink);position:relative;}
  .sheet{position:absolute;left:50px;width:1100px;height:774px;box-shadow:0 4px 14px rgba(0,0,0,.18);background:var(--paper);overflow:hidden;}
  .sheet--outside{top:769px;}
  .sheet--inside{top:1603px;}
  .spread{position:absolute;left:0;top:0;width:817px;height:575px;transform:scale(1.3464);transform-origin:0 0;}
  .spread svg.art{position:absolute;left:0;top:0;width:817px;height:575px;}
  .abs{position:absolute;}
  .brand-box{background:var(--panel-gray);display:flex;align-items:flex-end;justify-content:center;padding-bottom:22px;}
  .brand-name{font-family:"Poppins",sans-serif;font-weight:400;font-size:15px;letter-spacing:3.6px;color:var(--ink);white-space:nowrap;}
  .heading{font-weight:400;text-transform:uppercase;color:var(--ink);}
  .body-copy{font-size:10.6px;line-height:13.9px;text-align:justify;color:var(--ink-soft);}
  .contact{left:272px;width:276px;text-align:center;}
  .contact-phone{top:112px;font-size:19px;letter-spacing:.5px;}
  .contact-address{top:155px;font-size:12px;line-height:14.5px;}
  .contact-web{top:203px;font-size:12.5px;}
  .url-bar{background:#000;color:var(--gold-light);font-size:12.5px;text-align:center;line-height:24px;}
  .treatment-list{list-style:none;font-size:11px;line-height:18.5px;color:var(--ink-soft);}
  .treatment-list li{position:relative;padding-left:13px;}
  .treatment-list li::before{content:"";position:absolute;left:0;top:6px;border-left:7px solid var(--gold);border-top:3.5px solid transparent;border-bottom:3.5px solid transparent;}
  .rule{height:2px;background:var(--gold);}
  .why-bar{background:linear-gradient(90deg,var(--gold-dark),var(--gold));color:#fff;font-weight:600;font-size:13.5px;padding-left:8px;line-height:21px;letter-spacing:.4px;}
  .why-item{left:560px;width:245px;padding-left:40px;}
  .why-item h4{font-size:12px;font-weight:600;color:var(--gold);line-height:15px;}
  .why-item p{font-size:7.8px;line-height:9.8px;color:var(--ink-soft);margin-top:2px;}
  .why-icon{position:absolute;left:2px;top:1px;width:26px;height:26px;}
</style>
</head>
<body>

<!-- Outside spread -->
<section class="sheet sheet--outside" aria-label="Tri-fold outside">
  <div class="spread">
    <svg class="art" viewBox="0 0 817 575" aria-hidden="false">
      <defs>
        <linearGradient id="goldGrad" x1="0" y1="0" x2="1" y2="1">
          <stop offset="0" stop-color="#f2c46a"/><stop offset="1" stop-color="#b8862b"/>
        </linearGradient>
        <linearGradient id="doctorTone" x1="0" y1="0" x2="1" y2="1">
          <stop offset="0" stop-color="#d9d9d9"/><stop offset=".5" stop-color="#f4f4f4"/><stop offset="1" stop-color="#cfcfcf"/>
        </linearGradient>
        <linearGradient id="clinicTone" x1="0" y1="0" x2="1" y2="1">
          <stop offset="0" stop-color="#eef1f3"/><stop offset=".6" stop-color="#cfd9de"/><stop offset="1" stop-color="#b9a98f"/>
        </linearGradient>
      </defs>
      <!-- left panel -->
      <rect x="82" y="22" width="46" height="46" transform="rotate(45 105 45)" fill="#f2c46a"/>
      <polygon role="img" aria-label="Photo of a doctor in a white coat holding a stethoscope" points="0,150 78,78 118,114 162,68 405,352 298,306 0,300" fill="url(#doctorTone)"/>
      <polyline points="0,142 78,68 118,104 162,56 408,342" fill="none" stroke="#d9a43c" stroke-width="2.5"/>
      <polyline points="0,292 20,280 292,280 322,306" fill="none" stroke="#d9a43c" stroke-width="2.5"/>
      <polygon points="212,308 290,308 320,352 244,352" fill="url(#goldGrad)"/>
      <!-- middle panel icons -->
      <g fill="#e0a53b">
        <circle cx="371" cy="75" r="14"/><circle cx="410" cy="75" r="14"/><circle cx="449" cy="75" r="14"/>
      </g>
      <path d="M365 68c1-1 3-1 3 1l1 3c0 1-1 2-2 2 1 3 3 5 6 6 0-1 1-2 2-2l3 1c2 0 2 2 1 3l-2 2c-6 0-12-6-12-12z" fill="#fff"/>
      <path d="M410 65a6 6 0 0 1 6 6c0 5-6 11-6 11s-6-6-6-11a6 6 0 0 1 6-6z" fill="#fff"/>
      <circle cx="410" cy="71" r="2.2" fill="#e0a53b"/>
      <g fill="none" stroke="#fff" stroke-width="1.3">
        <circle cx="449" cy="75" r="7"/><ellipse cx="449" cy="75" rx="3" ry="7"/><line x1="442" y1="75" x2="456" y2="75"/>
      </g>
      <!-- right panel -->
      <rect x="673" y="137" width="40" height="40" transform="rotate(45 693 157)" fill="#f2c46a"/>
      <polygon role="img" aria-label="Photo of a bright modern clinic lobby with large windows" points="382,455 622,176 665,220 708,176 817,288 817,386 548,386 500,455" fill="url(#clinicTone)"/>
      <polyline points="372,458 622,162 665,206 708,162 817,270" fill="none" stroke="#d9a43c" stroke-width="2.5"/>
      <polyline points="470,475 552,392 817,392" fill="none" stroke="#d9a43c" stroke-width="2.5"/>
      <polygon points="775,412 817,412 817,466" fill="url(#goldGrad)"/>
    </svg>

    <h2 class="heading abs" style="left:28px;top:312px;font-size:23px;line-height:28px;">About Birchline<br>Wound Care</h2>
    <p class="body-copy abs" style="left:28px;top:396px;width:252px;">At Birchline Wound Care, we specialize in managing outpatient wound care facilities throughout the Dallas/Fort Worth area. Partnering with hospitals and local rehabilitation units, we deliver the most advanced wound care treatments. Our commitment to quality care resonates through our collaboration with small practice family providers, ensuring personalized, effective treatment plans.</p>

    <div class="contact abs contact-phone">555-014-2290</div>
    <div class="contact abs contact-address">1820 Cedar Knoll Rd Ste 200 PMB<br>410552 Dallas, TX 75230</div>
    <div class="contact abs contact-web">www.birchline-woundcare.com</div>

    <div class="brand-box abs" style="left:290px;top:432px;width:240px;height:143px;">
      <span class="brand-name" style="font-size:13px;letter-spacing:3px;">BIRCHLINE WOUNDCARE</span>
    </div>
    <div class="brand-box abs" style="left:566px;top:0;width:240px;height:130px;padding-bottom:40px;">
      <span class="brand-name" style="font-size:13px;letter-spacing:3px;">BIRCHLINE WOUNDCARE</span>
    </div>

    <h1 class="heading abs" style="left:560px;top:404px;width:240px;text-align:center;font-size:22.5px;line-height:29px;">Specialize in<br>Managing<br>Outpatient<br>Wound Care</h1>
    <div class="url-bar abs" style="left:558px;top:528px;width:244px;height:24px;">www.birchline-woundcare.com</div>
  </div>
</section>

<!-- Inside spread -->
<section class="sheet sheet--inside" aria-label="Tri-fold inside">
  <div class="spread">
    <svg class="art" viewBox="0 0 817 575">
      <defs>
        <linearGradient id="goldGrad2" x1="0" y1="0" x2="1" y2="1">
          <stop offset="0" stop-color="#f2c46a"/><stop offset="1" stop-color="#b8862b"/>
        </linearGradient>
        <linearGradient id="chamberTone" x1="0" y1="0" x2="1" y2="1">
          <stop offset="0" stop-color="#9a9a9a"/><stop offset=".5" stop-color="#ececec"/><stop offset="1" stop-color="#c9c9c9"/>
        </linearGradient>
        <linearGradient id="bandageTone" x1="0" y1="0" x2="1" y2="1">
          <stop offset="0" stop-color="#cfe0ea"/><stop offset=".5" stop-color="#f5f5f5"/><stop offset="1" stop-color="#d8a38e"/>
        </linearGradient>
        <linearGradient id="kneeTone" x1="0" y1="0" x2="1" y2="1">
          <stop offset="0" stop-color="#8fd0bb"/><stop offset=".5" stop-color="#e9c2a8"/><stop offset="1" stop-color="#f0f0f0"/>
        </linearGradient>
        <linearGradient id="handsTone" x1="0" y1="0" x2="1" y2="1">
          <stop offset="0" stop-color="#f4f4f4"/><stop offset="1" stop-color="#e3c0ad"/>
        </linearGradient>
      </defs>
      <!-- top photos -->
      <polygon role="img" aria-label="Photo of a patient resting inside a hyperbaric oxygen chamber" points="272,0 562,0 398,222 272,222" fill="url(#chamberTone)"/>
      <polygon role="img" aria-label="Photo of a clinician wrapping a bandage around a patient's knee" points="582,0 817,0 817,118 624,118 545,222 420,222" fill="url(#bandageTone)"/>
      <polyline points="568,0 404,226 272,226" fill="none" stroke="#d9a43c" stroke-width="2.5"/>
      <polyline points="545,226 627,122 817,122" fill="none" stroke="#d9a43c" stroke-width="2.5"/>
      <polygon points="775,178 817,178 817,232" fill="url(#goldGrad2)"/>
      <!-- bottom left -->
      <rect x="87" y="266" width="40" height="40" transform="rotate(45 107 286)" fill="#f2c46a"/>
      <polygon role="img" aria-label="Photo of a nurse examining a patient's knee" points="0,360 85,288 125,326 170,284 392,528 0,528" fill="url(#kneeTone)"/>
      <polyline points="0,350 85,278 125,316 170,272 400,528" fill="none" stroke="#d9a43c" stroke-width="2.5"/>
      <polyline points="0,560 22,536 300,536" fill="none" stroke="#d9a43c" stroke-width="2.5"/>
      <polygon points="232,543 287,543 302,575 247,575" fill="url(#goldGrad2)"/>
      <!-- bottom middle -->
      <polygon role="img" aria-label="Photo of a clinician's hands tending a patient's wrist" points="340,466 545,466 545,575 408,575" fill="url(#handsTone)"/>
    </svg>

    <h2 class="abs" style="left:22px;top:16px;width:250px;font-size:17.5px;line-height:22px;font-weight:400;">At Birchline Woundcare we specialize in treating a wide range of complex and hard-to-heal wounds.</h2>
    <div class="rule abs" style="left:22px;top:110px;width:230px;"></div>
    <p class="body-copy abs" style="left:22px;top:122px;width:248px;font-size:9.3px;line-height:12px;">Our expert team is equipped to care for atypical wounds, bone infections, burn wounds, chronic wounds, and diabetic ulcers. We also provide advanced care for non-healing surgical wounds, infected wounds, pilonidal cysts, pressure ulcers, and surgical wound complications. Additionally, we treat venous and arterial ulcers, including venous leg ulcers, using the latest techniques and personalized care plans to promote healing and prevent complications. No matter the wound type, our focus is on achieving optimal outcomes for every patient.</p>
    <div class="abs" style="left:40px;top:542px;font-size:11.5px;">www.birchline-woundcare.com</div>

    <h3 class="heading abs" style="left:290px;top:252px;font-size:21px;">Wound Treatment</h3>
    <div class="rule abs" style="left:290px;top:284px;width:220px;"></div>
    <ul class="treatment-list abs" style="left:290px;top:298px;width:250px;">
      <li>Compression Therapy</li>
      <li>Mechanical &amp; Enzymatic Debridement</li>
      <li>Negative Pressure Wound Therapy</li>
      <li>Post-Mohs Surgery</li>
      <li>Tissue Infection Management / Labs</li>
      <li>Total Contact Casting</li>
      <li>Wound Care</li>
      <li>Wound Debridement</li>
    </ul>

    <h3 class="heading abs" style="left:560px;top:196px;font-size:19.5px;line-height:24px;">Hyperbaric<br>Oxygen Therapy</h3>
    <div class="rule abs" style="left:560px;top:252px;width:218px;"></div>
    <p class="body-copy abs" style="left:560px;top:262px;width:242px;font-size:8.3px;line-height:10.4px;">A Cornerstone of Advanced Wound Care Hyperbaric Oxygen Therapy (HBO) is not just a treatment; it's a pivotal part of our comprehensive approach to wound healing at Birchline Wound Care. By delivering pure oxygen in a pressurized chamber, HBO therapy significantly increases the amount of oxygen in the blood, fostering an environment that accelerates the repair and regeneration of wounded tissues.</p>

    <div class="why-bar abs" style="left:560px;top:366px;width:242px;height:21px;">WHY CHOOSE US</div>

    <div class="why-item abs" style="top:397px;">
      <svg class="why-icon" viewBox="0 0 26 26" aria-hidden="true"><rect x="3" y="3" width="15" height="20" rx="1.5" fill="none" stroke="#d9a43c" stroke-width="1.6"/><line x1="6" y1="9" x2="15" y2="9" stroke="#d9a43c" stroke-width="1.4"/><line x1="6" y1="13" x2="13" y2="13" stroke="#d9a43c" stroke-width="1.4"/><circle cx="19" cy="18" r="5" fill="#d9a43c"/><path d="M17 18h4M19 16v4" stroke="#fff" stroke-width="1.4"/></svg>
      <h4>Accepted Health Plans</h4>
      <p>We accept most major insurance plans to make your care as accessible and affordable as possible!</p>
    </div>
    <div class="why-item abs" style="top:450px;">
      <svg class="why-icon" viewBox="0 0 26 26" aria-hidden="true"><circle cx="13" cy="6" r="3" fill="#d9a43c"/><circle cx="6" cy="9" r="2.4" fill="#d9a43c"/><circle cx="20" cy="9" r="2.4" fill="#d9a43c"/><rect x="3" y="14" width="20" height="9" fill="none" stroke="#d9a43c" stroke-width="1.6"/><line x1="9" y1="14" x2="9" y2="23" stroke="#d9a43c" stroke-width="1.4"/><line x1="17" y1="14" x2="17" y2="23" stroke="#d9a43c" stroke-width="1.4"/></svg>
      <h4>Expert Medical Team</h4>
      <p>Comprised of highly trained physicians, nurses, and specialists, our team brings years of experience in treating a wide range of complex wounds.</p>
    </div>
    <div class="why-item abs" style="top:510px;">
      <svg class="why-icon" viewBox="0 0 26 26" aria-hidden="true"><circle cx="13" cy="11" r="9" fill="none" stroke="#d9a43c" stroke-width="1.8"/><path d="M9 11l3 3 5-6" fill="none" stroke="#d9a43c" stroke-width="1.8"/><path d="M8 19l-2 6 4-2 3 2M18 19l2 6-4-2" fill="none" stroke="#d9a43c" stroke-width="1.4"/></svg>
      <h4>Trusted Healthcare</h4>
      <p>We specialize in advanced treatment modalities, using a multi-faceted approach to heal your patient's wound.</p>
    </div>
  </div>
</section>

</body>
</html>
```